Business Card Design for Consulting Company

I require a Business Card design for my Consulting company. <br/><br/>My company name is: Marcel Pruett Consulting Inc.<br/>My website is: www.marcelpruettconsulting.example<br/><br/>My company focuses on management and software development for the Tallyvane CRM platform (www.tallyvane.example)<br/><br/>I have a logo already designed...see attached.
Updates

Also Include my Name and Title: Marcel K.T. Pruett President

Target Market(s)

Tallyvane Customers

Contact Information for Business Card

Only include my LOGO (provided)
My Name: Marcel KT Pruett
My Title: President
My Company Name: Marcel Pruett Consulting Inc.
My Website: www.marcelpruettconsulting.example
My Email: marcel.pruett.consulting@mailbox.example

NO PHONE NUMBER
NO ADDRESS

Font styles to use
Serif
Sans Serif
Other font styles liked:
• see my website: www.marcelpruettconsulting.example

Colors

Designer to choose colors to be used in the design.

Requirements
Must have
• Must include my Orange
• Include my name (Marcel K.T. Pruett), title (President) company name, website and email
• It should also have a tag line like: Tallyvane Consulting
• I'm flexible with the tag line
Should not have
• Don't include my phone number or address

```html
<!DOCTYPE html>
<html lang="en">
<head>
<meta charset="utf-8">
<title>Marcel Pruett Consulting Inc. – Business Card</title>
<link href="https://fonts.googleapis.com/css2?family=Ubuntu:wght@400;500;700&display=swap" rel="stylesheet">
<style>
  :root {
    --orange: #f28122;
    --orange-light: #f7b27a;
    --ink: #2b2b2b;
    --grey: #8c8c8c;
    --paper: #ffffff;
    --backdrop: #2a2d31;
  }
  * { margin: 0; padding: 0; box-sizing: border-box; }
  html, body { width: 1200px; height: 900px; overflow: hidden; }
  body {
    background: var(--backdrop);
    font-family: "Ubuntu", sans-serif;
    position: relative;
  }
  .card {
    position: absolute;
    left: 285px;
    width: 630px;
    height: 360px;
    overflow: hidden;
    box-shadow: 0 10px 30px rgba(0,0,0,.35);
  }
  .card--front { top: 60px; background: var(--paper); }
  .card--back { top: 480px; background: var(--orange); }

  .accent-bar { position: absolute; left: 40px; width: 9px; }
  .accent-bar--name { top: 32px; height: 78px; background: var(--orange); }
  .accent-bar--company { top: 182px; height: 64px; background: var(--grey); }

  .identity { position: absolute; left: 64px; top: 32px; }
  .identity__name {
    color: var(--orange); font-weight: 700; font-size: 25px;
    text-transform: uppercase; letter-spacing: -.3px;
  }
  .identity__title { color: var(--ink); font-size: 21px; margin-top: 2px; }

  .contact { position: absolute; left: 64px; top: 124px; list-style: none; }
  .contact__item {
    display: flex; align-items: center; gap: 9px;
    color: var(--ink); font-size: 15px; line-height: 24px;
  }
  .contact__icon { width: 13px; height: 13px; flex: none; }

  .company { position: absolute; left: 64px; top: 186px; width: 320px; }
  .company__name { color: var(--orange); font-weight: 500; font-size: 24px; white-space: nowrap; }
  .company__about { color: var(--ink); font-size: 14px; line-height: 20px; margin-top: 4px; }
  .company__link { color: var(--orange); }

  .brandmark {
    position: absolute; right: 84px; top: 232px;
    display: flex; align-items: center; gap: 10px;
    color: var(--orange); font-weight: 700; font-size: 18px;
  }
  .brandmark__square { width: 16px; height: 16px; background: var(--orange); }

  .corner-block {
    position: absolute; right: 0; bottom: 0;
    width: 64px; height: 104px; background: var(--orange);
  }

  .back-mark {
    position: absolute; inset: 0;
    display: flex; align-items: center; justify-content: center; gap: 18px;
    color: var(--orange-light); font-weight: 700; font-size: 40px;
  }
  .back-mark__square { width: 36px; height: 36px; background: var(--orange-light); }
</style>
</head>
<body>
  <section class="card card--front" aria-label="Business card front">
    <div class="accent-bar accent-bar--name"></div>
    <header class="identity">
      <h1 class="identity__name">Marcel KT Pruett</h1>
      <p class="identity__title">President</p>
    </header>
    <ul class="contact">
      <li class="contact__item">
        <svg class="contact__icon" viewBox="0 0 14 14" aria-hidden="true">
          <rect x="0.5" y="2.5" width="13" height="9" fill="#f28122"/>
          <path d="M1 3 L7 8 L13 3" fill="none" stroke="#fff" stroke-width="1.3"/>
        </svg>
        marcel.pruett.consulting@mailbox.example
      </li>
      <li class="contact__item">
        <svg class="contact__icon" viewBox="0 0 14 14" aria-hidden="true">
          <circle cx="7" cy="7" r="6.5" fill="#f28122"/>
          <ellipse cx="7" cy="7" rx="2.6" ry="6" fill="none" stroke="#fff" stroke-width="1"/>
          <path d="M1 7 H13" stroke="#fff" stroke-width="1"/>
        </svg>
        www.marcelpruettconsulting.example
      </li>
    </ul>
    <div class="accent-bar accent-bar--company"></div>
    <div class="company">
      <h2 class="company__name">Marcel Pruett Consulting Inc.</h2>
      <p class="company__about">My company focuses on management and software development for the Tallyvane CRM platform <span class="company__link">www.tallyvane.example</span></p>
    </div>
    <div class="brandmark">
      <span class="brandmark__square"></span>
      <span>Marcel Pruett</span>
    </div>
    <div class="corner-block"></div>
  </section>

  <section class="card card--back" aria-label="Business card back">
    <div class="back-mark">
      <span class="back-mark__square"></span>
      <span>Marcel Pruett</span>
    </div>
  </section>
</body>
</html>
```